Tallbridge needs a new rocket based website

We need a new website that will be based on our rocket ship logo. We develop innovative solutions for enterprises. We would like to see a design that when the pages scroll, the rocket launches and goes from launch through a journey, similar to how we approach our customer. We would like areas for "Who are we", "What can we do", "What have we done", "How can we help". http://www.tallbridge.com.au is our current website

Target Market(s)

Government, Enterprise, Cloud

Industry/Entity Type

Software Service

Coding

Coded - Design and coding required

Number of Pages Required

2 page

Requirements
Must have
• We would like to see a design that when the pages scroll, the rocket launches and goes from launch through a journey, similar to how we approach our customer.
• Must have a home page and a detail page.
• Would like to see the logo/rocket animate in some way when you scroll through he page.

```html
<!DOCTYPE html>
<html lang="en">
<head>
<meta charset="utf-8">
<title>Tallbridge</title>
<link rel="stylesheet" href="https://fonts.googleapis.com/css2?family=Open+Sans:wght@400;600;700&display=swap">
<style>
  :root {
    --orange: #f7931e;
    --orange-soft: #fde3c4;
    --ink: #333333;
    --text: #4a4a4a;
    --muted: #8a8a8a;
    --page: #f3f3f3;
    --card: #ffffff;
    --line: #e2e2e2;
    --photo: #d9d4cf;
  }
  * { box-sizing: border-box; margin: 0; padding: 0; }
  html, body { width: 1200px; height: 2261px; overflow: hidden; }
  body {
    position: relative;
    background: var(--page);
    font-family: "Open Sans", Arial, sans-serif;
    color: var(--text);
  }
  .abs { position: absolute; }
  .accent { color: var(--orange); }

  /* header */
  .brand {
    position: absolute; display: flex; align-items: center; gap: 8px;
    font-weight: 700; color: var(--ink); font-size: 38px; letter-spacing: -0.5px;
  }
  .brand-dot { width: 14px; height: 14px; border-radius: 50%; background: var(--orange); }
  .site-brand { left: 0; right: 0; justify-content: center; top: 38px; }
  .menu-toggle { left: 1093px; top: 52px; width: 26px; }
  .menu-toggle span { display: block; height: 4px; background: var(--orange); margin-bottom: 4px; border-radius: 1px; }

  .section-title {
    position: absolute; left: 0; right: 0; text-align: center;
    font-size: 29px; font-weight: 600; color: var(--ink);
  }

  /* about */
  .about-title { left: 81px; top: 180px; font-size: 30px; font-weight: 600; color: var(--ink); }
  .tabs { left: 80px; top: 234px; display: flex; gap: 10px; }
  .tab {
    height: 36px; padding: 0 6px; border: 2px solid #cfcfcf; background: var(--page);
    font-size: 14px; color: var(--text); line-height: 32px; text-transform: uppercase;
    text-align: center; white-space: nowrap;
  }
  .tab.is-active { background: var(--orange); border-color: var(--orange); color: #fff; }
  .tab-what { width: 132px; }
  .tab-mission { width: 123px; }
  .tab-goal { width: 123px; }
  .about-copy { left: 81px; top: 288px; width: 480px; font-size: 14px; line-height: 17px; color: var(--text); }
  .about-copy p { margin-bottom: 17px; }
  .about-art {
    left: 626px; top: 150px; width: 452px; height: 385px;
    background: radial-gradient(ellipse at 55% 60%, var(--orange-soft) 0%, rgba(253,227,196,0.35) 55%, rgba(243,243,243,0) 75%);
  }

  /* team */
  .team-card { top: 701px; width: 238px; height: 274px; background: var(--card); text-align: center; }
  .team-photo {
    position: absolute; left: 21px; top: -18px; width: 196px; height: 196px;
    background: linear-gradient(180deg, #ececec 0%, var(--photo) 100%);
  }
  .team-name { position: absolute; left: 0; right: 0; top: 185px; font-size: 15px; font-weight: 600; color: var(--orange); }
  .team-role { position: absolute; left: 0; right: 0; top: 206px; font-size: 15px; color: var(--ink); }
  .team-rule { position: absolute; left: 59px; right: 59px; top: 234px; height: 1px; background: var(--line); }
  .team-social { position: absolute; left: 0; right: 0; top: 246px; display: flex; justify-content: center; gap: 10px; }
  .team-social span { width: 6px; height: 6px; border-radius: 50%; background: var(--ink); }

  /* clients */
  .client-card { top: 1150px; width: 328px; height: 226px; background: var(--card); text-align: center; }
  .client-avatar {
    position: absolute; left: 107px; top: -60px; width: 114px; height: 114px; border-radius: 50%;
    border: 4px solid #fff; background: linear-gradient(180deg, #e8ecef 0%, var(--photo) 100%);
  }
  .client-name { position: absolute; left: 0; right: 0; top: 78px; font-size: 18px; font-weight: 600; color: var(--ink); }
  .client-role { position: absolute; left: 0; right: 0; top: 101px; font-size: 14px; color: var(--orange); }
  .client-quote { position: absolute; left: 42px; right: 42px; top: 132px; font-size: 13px; line-height: 17px; color: var(--ink); }
  .quote-mark { position: absolute; font-size: 28px; font-weight: 700; color: var(--ink); line-height: 1; }
  .quote-open { left: 40px; top: 122px; }
  .quote-close { right: 46px; top: 180px; }
  .carousel-dots { left: 0; right: 0; top: 1414px; display: flex; justify-content: center; gap: 8px; }
  .carousel-dots span { width: 7px; height: 7px; border-radius: 50%; background: #b5b5b5; }
  .carousel-dots span.is-active { background: var(--orange); }

  /* contact */
  .field {
    position: absolute; background: var(--card); font-size: 15px; color: var(--text);
    padding: 0 18px; line-height: 38px;
  }
  .field-message { line-height: 1; padding-top: 16px; }
  .send-button {
    left: 534px; top: 1831px; width: 129px; height: 37px; background: var(--orange);
    color: #fff; font-size: 15px; text-align: center; line-height: 37px; text-transform: uppercase;
  }

  /* footer */
  .footer-brand { left: 0; right: 0; justify-content: center; top: 1910px; font-size: 42px; }
  .contact-item { top: 1992px; width: 220px; text-align: center; font-size: 15px; line-height: 18px; color: var(--ink); }
  .contact-icon {
    width: 72px; height: 72px; border-radius: 50%; background: var(--orange);
    margin: 0 auto 12px; display: flex; align-items: center; justify-content: center;
  }
  .footer-social { left: 0; right: 0; top: 2134px; display: flex; justify-content: center; gap: 10px; }
  .footer-social span { width: 33px; height: 33px; border-radius: 50%; }
  .footer-rule { left: 0; right: 0; top: 2190px; height: 1px; background: #dcdcdc; }
  .copyright { left: 0; right: 0; top: 2215px; text-align: center; font-size: 14px; color: var(--ink); }
</style>
</head>
<body>

<header>
  <div class="brand site-brand"><span class="brand-dot"></span>Tallbridge</div>
  <div class="abs menu-toggle"><span></span><span></span><span></span></div>
</header>

<section class="about">
  <h2 class="abs about-title">Who <span class="accent">are we</span></h2>
  <div class="abs tabs">
    <div class="tab tab-what is-active">What we do</div>
    <div class="tab tab-mission">Our Mission</div>
    <div class="tab tab-goal">Our Goal</div>
  </div>
  <div class="abs about-copy">
    <p>Lorem Ipsum is simply dummy text of the printing and typesetting industry. Lorem Ipsum has been the industry's and standard dummy text ever since the 1500s,</p>
    <p>when an unknown printer took a galley of type and scrambled it to make a type specimen book. It has survived not only five centuries, but also the leap into electronic typesetting, remaining essentially unchanged.</p>
    <p>Lorem Ipsum is simply dummy text of the printing and typesetting industry. Lorem Ipsum has been the industry's and standard dummy text ever since the 1500s.</p>
  </div>
  <div class="abs about-art" role="img" aria-label="Orange line illustration of a laptop and phone with a rocket, surrounded by cloud, gear and code icons"></div>
</section>

<section class="team">
  <h2 class="section-title" style="top:604px">Meet <span class="accent">Our Team</span></h2>
  <article class="abs team-card" style="left:81px">
    <div class="team-photo" role="img" aria-label="Portrait photo of a team member"></div>
    <div class="team-name">Full Name</div><div class="team-role">Chief Executive Officer</div>
    <div class="team-rule"></div><div class="team-social"><span></span><span></span><span></span><span></span></div>
  </article>
  <article class="abs team-card" style="left:344px">
    <div class="team-photo" role="img" aria-label="Portrait photo of a team member"></div>
    <div class="team-name">Full Name</div><div class="team-role">Chief Executive Officer</div>
    <div class="team-rule"></div><div class="team-social"><span></span><span></span><span></span><span></span></div>
  </article>
  <article class="abs team-card" style="left:609px">
    <div class="team-photo" role="img" aria-label="Portrait photo of a team member"></div>
    <div class="team-name">Full Name</div><div class="team-role">Chief Executive Officer</div>
    <div class="team-rule"></div><div class="team-social"><span></span><span></span><span></span><span></span></div>
  </article>
  <article class="abs team-card" style="left:876px">
    <div class="team-photo" role="img" aria-label="Portrait photo of a team member"></div>
    <div class="team-name">Full Name</div><div class="team-role">Chief Executive Officer</div>
    <div class="team-rule"></div><div class="team-social"><span></span><span></span><span></span><span></span></div>
  </article>
</section>

<section class="clients">
  <h2 class="section-title" style="top:1031px">Our <span class="accent">Clients</span></h2>
  <article class="abs client-card" style="left:83px">
    <div class="client-avatar" role="img" aria-label="Round portrait photo of a client"></div>
    <div class="client-name">Marcus Hale</div><div class="client-role">Creative Director</div>
    <span class="quote-mark quote-open">&ldquo;</span>
    <p class="client-quote">Lorem Ipsum is simply dummy text typesetting industry. Lorem Ipsum in the standard dummy.</p>
    <span class="quote-mark quote-close">&rdquo;</span>
  </article>
  <article class="abs client-card" style="left:437px">
    <div class="client-avatar" role="img" aria-label="Round portrait photo of a client"></div>
    <div class="client-name">Elena Marsh</div><div class="client-role">Creative Director</div>
    <span class="quote-mark quote-open">&ldquo;</span>
    <p class="client-quote">Lorem Ipsum is simply dummy text typesetting industry. Lorem Ipsum in the standard dummy</p>
    <span class="quote-mark quote-close">&rdquo;</span>
  </article>
  <article class="abs client-card" style="left:790px">
    <div class="client-avatar" role="img" aria-label="Round portrait photo of a client"></div>
    <div class="client-name">Owen Pritchard</div><div class="client-role">Creative Director</div>
    <span class="quote-mark quote-open">&ldquo;</span>
    <p class="client-quote">Lorem Ipsum is simply dummy text typesetting industry. Lorem Ipsum in the standard dummy</p>
    <span class="quote-mark quote-close">&rdquo;</span>
  </article>
  <div class="abs carousel-dots"><span class="is-active"></span><span></span><span></span></div>
</section>

<section class="contact">
  <h2 class="section-title" style="top:1449px">Quick <span class="accent">Contact</span></h2>
  <div class="field" style="left:231px;top:1530px;width:352px;height:38px">First Name</div>
  <div class="field" style="left:611px;top:1530px;width:351px;height:38px">Last Name</div>
  <div class="field" style="left:231px;top:1592px;width:352px;height:39px">Email</div>
  <div class="field" style="left:611px;top:1592px;width:351px;height:39px">Phone</div>
  <div class="field field-message" style="left:231px;top:1658px;width:733px;height:148px">How can we Help?</div>
  <div class="abs send-button">Send</div>
</section>

<footer>
  <div class="brand footer-brand"><span class="brand-dot"></span>Tallbridge</div>
  <div class="abs contact-item" style="left:271px">
    <div class="contact-icon">
      <svg width="34" height="34" viewBox="0 0 24 24" fill="none" stroke="#fff" stroke-width="1.8" stroke-linejoin="round"><path d="M5 3h4l2 5-2.5 1.5a11 11 0 0 0 6 6L16 13l5 2v4a2 2 0 0 1-2 2A16 16 0 0 1 3 5a2 2 0 0 1 2-2z"/></svg>
    </div>
    1300 482 610
  </div>
  <div class="abs contact-item" style="left:487px">
    <div class="contact-icon">
      <svg width="34" height="34" viewBox="0 0 24 24" fill="none" stroke="#fff" stroke-width="1.8" stroke-linejoin="round"><path d="M3 11l9-7 9 7M5 9.5V20h14V9.5"/><path d="M10 20v-5h4v5"/></svg>
    </div>
    Unit 7, 48 Kestrel Rd<br>Linden Park, SA 5065
  </div>
  <div class="abs contact-item" style="left:704px">
    <div class="contact-icon">
      <svg width="36" height="36" viewBox="0 0 24 24" fill="none" stroke="#fff" stroke-width="1.6" stroke-linejoin="round"><rect x="3" y="6" width="18" height="12"/><path d="M3 6l9 7 9-7M3 18l7-6M21 18l-7-6"/></svg>
    </div>
    info@tallbridge.com.au
  </div>
  <div class="abs footer-social">
    <span style="background:#3b5998"></span><span style="background:#1da1f2"></span><span style="background:#0e76a8"></span><span style="background:#333"></span>
  </div>
  <div class="abs footer-rule"></div>
  <p class="abs copyright">Copyright &copy; Tallbridge 2018. All Rights Reserved.</p>
</footer>

</body>
</html>
```